Electrical Contracting business card design

We need a simple business card design for an Electrical Contracting business. A simple design would be appreciated
This company has 2 directors so on one it would have Dale Morrow & another with Shane Morrow.
Updates

Project Deadline Extended
Reason: Hello A few designers have asked for a logo unfortunately we don't have one so have extended deadline to see who can help us out with this. CHEERS

Project Deadline Extended
Reason: Waiting for business partner to return from xmas break. cheers

Industry/Entity Type

Business

Contact Information for Business Card

Quolvin Electrical Services P/L
REC: 63417
Residential Commercial Industrial
Service-Repairs-Renovations-Installations-Telephone-Data
Dale Morrow-Ph: 0437 612 388
Email: dale@quolvinelectrical.com.au

Requirements
Should not have
• The design should not have any electrical appliances in it ie: power-points, leads, houses etc.

```html
<!DOCTYPE html>
<html lang="en">
<head>
<meta charset="utf-8">
<title>Quolvin Electrical Services – Dale Morrow</title>
<link href="https://fonts.googleapis.com/css2?family=Jost:wght@300;400&display=swap" rel="stylesheet">
<style>
  :root {
    --teal-text: #1f6e66;
    --teal-band: #21917f;
    --paper: #ffffff;
    --accent-orange: #ea8a4c;
    --white: #ffffff;
  }
  html, body {
    margin: 0;
    padding: 0;
    width: 1200px;
    height: 741px;
    overflow: hidden;
    background: var(--paper);
  }
  .card {
    position: relative;
    width: 1200px;
    height: 741px;
    background: var(--paper);
    font-family: "Jost", "Helvetica Neue", Arial, sans-serif;
    color: var(--teal-text);
  }
  .services {
    position: absolute;
    left: 0;
    width: 1200px;
    text-align: center;
    font-weight: 400;
    font-size: 25px;
    letter-spacing: 2.6px;
    white-space: pre;
    margin: 0;
    line-height: 1;
  }
  .services--company { top: 48px; }
  .services--trades { top: 89px; }
  .brand {
    position: absolute;
    top: 300px;
    left: 0;
    width: 1200px;
    text-align: center;
    font-weight: 400;
    font-size: 50px;
    letter-spacing: 8px;
    line-height: 1;
    color: var(--teal-text);
    margin: 0;
  }
  .horizon {
    position: absolute;
    top: 385px;
    left: 378px;
    width: 440px;
    height: 2px;
    background: linear-gradient(90deg, rgba(234,138,76,0) 0%, var(--accent-orange) 35%, var(--accent-orange) 65%, rgba(234,138,76,0) 100%);
  }
  .director {
    position: absolute;
    top: 410px;
    left: 0;
    width: 1200px;
    text-align: center;
    font-weight: 300;
    font-size: 54px;
    letter-spacing: 4px;
    line-height: 1;
    margin: 0;
  }
  .infoline {
    position: absolute;
    top: 470px;
    left: 0;
    width: 1200px;
    text-align: center;
    font-weight: 400;
    font-size: 27px;
    letter-spacing: 2.4px;
    line-height: 1;
    margin: 0;
  }
  .email-band {
    position: absolute;
    top: 659px;
    left: 0;
    width: 1200px;
    height: 37px;
    background: var(--teal-band);
    display: flex;
    align-items: center;
    justify-content: center;
  }
  .email {
    color: var(--white);
    font-weight: 400;
    font-size: 26px;
    letter-spacing: 2.4px;
    line-height: 1;
  }
</style>
</head>
<body>
  <main class="card">
    <p class="services services--company">QUOLVIN ELECTRICAL SERVICES  RESIDENTIAL  COMMERCIAL INDUSTRIAL</p>
    <p class="services services--trades">P/L REC: 63417 REPAIRS - RENOVATIONS - INSTALLATIONS - TELEPHONE</p>

    <p class="brand">QUOLVIN</p>
    <div class="horizon"></div>

    <h1 class="director">DALE MORROW</h1>
    <p class="infoline">INFOLINE 0437 612 388</p>

    <div class="email-band">
      <span class="email">EMAIL: DALE@QUOLVINELECTRICAL.COM.AU</span>
    </div>
  </main>
</body>
</html>
```